Real estate broker business card

Want a modern celan but effective business card for my residential and commercial real estate business. I want the back of the card to advertise my services and to capture business. I have attached the back of my current business card fore ideas
Updates

Target Market(s)

home buyers and seller. commercial buyers and sellers

Industry/Entity Type

Real Estate

Contact Information for Business Card

must have my contact information and my photo

Requirements
Must have
• Lorna Vettridge
• Owner & Qualifying Broker
• Brockhill Real Estate Services
• 555.218.7094
• lorna@brockhillhomes.example
• www.brockhillhomes.example
Nice to have
• metallic
• Business capture text: " Don't buy or lease property without someone looking out for your best interests. I will represent you on your home or investment purchase for FREE!"
• "Home owners, call today to receive a FREE market analysis for your homes value!

```html
<!DOCTYPE html>
<html lang="en">
<head>
<meta charset="utf-8">
<title>Brockhill Real Estate Services – Business Card</title>
<link rel="stylesheet" href="https://fonts.googleapis.com/css2?family=Libre+Baskerville:wght@400;700&display=swap">
<style>
  :root {
    --backdrop: #e6e6e4;
    --card-white: #f7f7f7;
    --teal: #1e98a6;
    --teal-light: #45b9c6;
    --teal-deep: #167f8c;
    --ink-white: #ffffff;
    --photo-dark: #3a3a2a;
    --photo-light: #8a7e70;
    --shadow: rgba(0, 0, 0, 0.18);
  }
  * { box-sizing: border-box; margin: 0; padding: 0; }
  html, body {
    width: 1200px; height: 800px; overflow: hidden;
    background: var(--backdrop);
    font-family: "Libre Baskerville", Georgia, serif;
  }
  .canvas { position: relative; width: 1200px; height: 800px; }

  .card {
    position: absolute;
    width: 560px; height: 320px;
    background: var(--card-white);
    box-shadow: 0 10px 28px var(--shadow);
    display: flex;
    overflow: hidden;
  }
  .card--front { left: 80px; top: 70px; }
  .card--back { left: 560px; top: 410px; }

  .portrait {
    width: 44%; height: 100%;
    background: linear-gradient(160deg, var(--photo-dark), var(--photo-light) 70%, #d8d2cc);
  }

  .brand-side {
    flex: 1;
    display: flex; flex-direction: column;
    align-items: center; justify-content: center;
    gap: 12px;
  }
  .card--back .brand-side { flex: 0 0 45%; }
  .brand-mark {
    width: 46px; height: 46px; border-radius: 50%;
    background: linear-gradient(145deg, var(--teal-light), var(--teal-deep));
  }
  .brand-name {
    color: var(--teal);
    font-weight: 400;
    text-align: center;
    text-transform: uppercase;
    line-height: 1.25;
  }
  .brand-name .primary { display: block; font-size: 30px; letter-spacing: 1px; }
  .brand-name .secondary { display: block; font-size: 11px; letter-spacing: 2.5px; }

  .contact-panel {
    flex: 1;
    background: linear-gradient(135deg, var(--teal-light), var(--teal) 55%, var(--teal-deep));
    color: var(--ink-white);
    padding: 56px 26px 0 26px;
  }
  .agent-name { font-size: 21px; font-weight: 700; }
  .agent-title { font-size: 12px; margin-top: 4px; }
  .contact-list { list-style: none; margin-top: 40px; display: flex; flex-direction: column; gap: 14px; }
  .contact-item { display: flex; align-items: center; gap: 12px; font-size: 12.5px; }
  .contact-icon {
    width: 24px; height: 24px; flex: none;
    background: var(--ink-white);
    display: flex; align-items: center; justify-content: center;
  }
  .contact-icon svg { width: 14px; height: 14px; }
</style>
</head>
<body>
<main class="canvas">

  <section class="card card--front" aria-label="Card front">
    <div class="portrait" role="img" aria-label="Portrait photo of the broker"></div>
    <div class="brand-side">
      <span class="brand-mark"></span>
      <p class="brand-name"><span class="primary">Brockhill</span><span class="secondary">Real Estate Services</span></p>
    </div>
  </section>

  <section class="card card--back" aria-label="Card back">
    <div class="brand-side">
      <span class="brand-mark"></span>
      <p class="brand-name"><span class="primary">Brockhill</span><span class="secondary">Real Estate Services</span></p>
    </div>
    <div class="contact-panel">
      <h1 class="agent-name">Lorna Vettridge</h1>
      <p class="agent-title">Owner &amp; Qualifying Broker</p>
      <ul class="contact-list">
        <li class="contact-item">
          <span class="contact-icon"><svg viewBox="0 0 16 16"><path fill="#1e98a6" d="M4 1l2.5 3-1.5 1.5c.8 2 2.5 3.7 4.5 4.5L11 8.5 14 11l-1.5 3C7 13.5 2.5 9 2 3.5z"/></svg></span>
          555.218.7094
        </li>
        <li class="contact-item">
          <span class="contact-icon"><svg viewBox="0 0 16 16"><rect x="1.5" y="3.5" width="13" height="9" fill="none" stroke="#1e98a6" stroke-width="1.5"/><path d="M1.5 3.5L8 9l6.5-5.5" fill="none" stroke="#1e98a6" stroke-width="1.5"/></svg></span>
          lorna@brockhillhomes.example
        </li>
        <li class="contact-item">
          <span class="contact-icon"><svg viewBox="0 0 16 16"><circle cx="8" cy="8" r="6.2" fill="none" stroke="#1e98a6" stroke-width="1.4"/><ellipse cx="8" cy="8" rx="2.6" ry="6.2" fill="none" stroke="#1e98a6" stroke-width="1.2"/><path d="M1.8 8h12.4" stroke="#1e98a6" stroke-width="1.2"/></svg></span>
          www.brockhillhomes.example
        </li>
      </ul>
    </div>
  </section>

</main>
</body>
</html>
```